TRAVIM 2026 Flyer for Conference

TRAVIM needs a design for a 1-page flyer that we will hand out at an upcoming event & then later post online as a pdf. There are 3 elements which need to be on the flyer:

1) A logo. This should be prominent on the design (e.g., in the middle). The flyer should use the colors that are in that logo (e.g., for accents, design elements, and/or text; not all of these have to be used):
Dark blue: #185577
Med blue: #327C9A
Teal: #4EB1C2
Light Teal: #9EDBE6

2) The conference theme -- Oceans of Knowledge: Diving into Information Literacy -- should be at the flyer's top.

3) Finally, these six tracks should be listed below the theme and the logo (it's font size should be at least a couple sizes smaller than the size used for the theme):
- Pearls of Pedagogy: Teaching Techniques that Work
- The Depth Gauge: Measuring Instructional Impact
- Techtonic Shifts: Innovation and Educational Technology
- Captain's Log: Navigating Leadership in Library Instruction
- Swimming Together: Collaborating with Others
- The Bermuda Triangle: Exploring (Seemingly) Eternal Challenges

Font styles to use
Sans Serif

Colors
0094D4
00A9DD
6FCCEA
C7EBF8
E9F6FB

Requirements
Must have
• The 3 elements listed in the description: 1) the logo, 2) the text of the theme and 3) the text for the tracks.

```html
<!DOCTYPE html>
<html lang="en">
<head>
<meta charset="utf-8">
<title>TRAVIM 2026 – Oceans of Knowledge</title>
<link href="https://fonts.googleapis.com/css2?family=Poppins:wght@400;500;600;800;900&family=Fira+Sans:wght@400;600&display=swap" rel="stylesheet">
<style>
  :root {
    --page-bg: #efefef;
    --deep-navy: #04131c;
    --deep-teal: #0b4a5e;
    --ocean-mid: #0f6f86;
    --dark-blue: #185577;
    --med-blue: #327C9A;
    --teal: #4EB1C2;
    --light-teal: #9EDBE6;
    --cyan: #00c8e6;
    --bright-blue: #0094D4;
    --card: #52c6df;
    --card-ink: #0e2b3a;
    --white: #ffffff;
  }
  * { margin: 0; padding: 0; box-sizing: border-box; }
  html, body { width: 1031px; height: 1200px; overflow: hidden; }
  body {
    background: var(--page-bg);
    font-family: "Poppins", sans-serif;
    display: flex;
    justify-content: center;
  }
  .flyer {
    position: relative;
    width: 928px;
    height: 1200px;
    overflow: hidden;
    background:
      radial-gradient(ellipse 55% 38% at 50% 0%, rgba(30,170,200,0.75), transparent 75%),
      radial-gradient(ellipse 70% 30% at 50% 88%, rgba(40,80,80,0.45), transparent 80%),
      linear-gradient(180deg, var(--ocean-mid) 0%, var(--deep-teal) 28%, #062a38 55%, var(--deep-navy) 100%);
  }
  .brand {
    position: absolute;
    top: 92px;
    left: 0; right: 0;
    display: flex;
    justify-content: center;
    align-items: center;
    gap: 12px;
  }
  .brand-dot {
    width: 18px; height: 18px;
    border-radius: 50%;
    background: var(--light-teal);
  }
  .brand-name {
    font-family: "Poppins", sans-serif;
    font-weight: 800;
    font-size: 44px;
    letter-spacing: 1px;
    color: var(--light-teal);
  }
  .brand-meta {
    position: absolute;
    top: 160px;
    left: 0; right: 0;
    text-align: center;
    font-size: 12px;
    letter-spacing: 3px;
    color: var(--light-teal);
    font-weight: 500;
  }
  .theme-title {
    position: absolute;
    top: 236px;
    left: 0; right: 0;
    text-align: center;
    font-weight: 800;
    font-size: 138px;
    line-height: 1.1;
    letter-spacing: -2px;
    background: linear-gradient(90deg, #0aa7d8 0%, var(--cyan) 30%, #17c4e0 60%, var(--med-blue) 100%);
    -webkit-background-clip: text;
    background-clip: text;
    color: transparent;
  }
  .theme-sub {
    position: absolute;
    top: 366px;
    left: 0; right: 0;
    text-align: center;
    font-weight: 800;
    font-size: 38px;
    letter-spacing: 18px;
    padding-left: 18px;
    color: var(--white);
  }
  .theme-tagline {
    position: absolute;
    top: 418px;
    left: 0; right: 0;
    text-align: center;
    font-size: 23px;
    font-weight: 400;
    color: var(--white);
  }
  .tracks {
    position: absolute;
    top: 472px;
    left: 89px;
    width: 750px;
    display: grid;
    grid-template-columns: repeat(3, 1fr);
    column-gap: 17px;
    row-gap: 22px;
  }
  .track {
    height: 102px;
    border-radius: 16px;
    background: linear-gradient(180deg, var(--card) 0%, #5acde4 100%);
    display: flex;
    flex-direction: column;
    align-items: center;
    justify-content: center;
    text-align: center;
    padding: 0 10px 6px;
    color: var(--card-ink);
  }
  .track-title {
    font-family: "Fira Sans", sans-serif;
    font-weight: 600;
    font-size: 21px;
    white-space: nowrap;
  }
  .track-desc {
    margin-top: 8px;
    font-size: 11.5px;
    line-height: 1.2;
    max-width: 160px;
  }
  .book-art {
    position: absolute;
    top: 755px;
    left: 93px;
    width: 770px;
    height: 342px;
    border-radius: 50% 50% 6px 6px / 30% 30% 6px 6px;
    background:
      radial-gradient(ellipse 22% 45% at 50% 45%, rgba(200,230,240,0.55), transparent 80%),
      linear-gradient(180deg, rgba(200,160,110,0.0) 0%, rgba(196,160,112,0.55) 40%, rgba(120,95,70,0.55) 80%, rgba(20,30,35,0.2) 100%);
  }
  .site-url {
    position: absolute;
    top: 1100px;
    left: 0; right: 0;
    text-align: center;
    font-size: 29px;
    font-weight: 500;
    letter-spacing: 15px;
    padding-left: 15px;
    color: var(--white);
  }
  .site-url .domain { color: var(--cyan); font-weight: 600; }
</style>
</head>
<body>
  <main class="flyer">
    <div class="brand">
      <span class="brand-dot"></span>
      <span class="brand-name">TRAVIM 2026</span>
    </div>
    <p class="brand-meta">NORFOLK, VA · MAY 7-9</p>

    <h1 class="theme-title">OCEANS</h1>
    <p class="theme-sub">OF KNOWLEDGE</p>
    <p class="theme-tagline">Diving into Information Literacy</p>

    <section class="tracks">
      <div class="track"><h2 class="track-title">Pearls of Pedagogy</h2><p class="track-desc">Teaching Techniques that Work</p></div>
      <div class="track"><h2 class="track-title">The Depth Gauge</h2><p class="track-desc">Measuring Instructional Impact</p></div>
      <div class="track"><h2 class="track-title">Techtonic Shifts</h2><p class="track-desc">Innovation and Educational Technology</p></div>
      <div class="track"><h2 class="track-title">Captain's Log</h2><p class="track-desc">Navigating Leadership in Library Instruction</p></div>
      <div class="track"><h2 class="track-title">Swimming Together</h2><p class="track-desc" style="max-width:200px">Collaborating with Others</p></div>
      <div class="track"><h2 class="track-title">The Bermuda Triangle</h2><p class="track-desc">Exploring (Seemingly) Eternal Challenges</p></div>
    </section>

    <div class="book-art" role="img" aria-label="Photo of an open book with fanned pages glowing on the sea floor"></div>

    <p class="site-url">www.<span class="domain">travim2026</span>.com</p>
  </main>
</body>
</html>
```